Hello,
We’re looking for a new WordPress website for Gather Your Light, our company offering unique well-being retreats and workshops.
We currently have a website online (you can consult it : www.gatheryourlight.ch), but we now need to build a new site on WordPress — more flexible, more intuitive to manage, and better aligned with our evolving needs.

What we’re looking for:
A new userfriendly WordPress site, with:
Inspiring, elegant, and modern design
Smooth user experience on desktop and mobile
Innovative design proposals – we want to be inspired !
SEO best practices
Respect of our existing color palette
The final website will need to be set up on our existing hosting provider (details can be shared later)

Pages to Include:
- Home
- Our Story
- Our Stays - with links to 5 individual pages, each describing one of our stays in detail.
- Activities – with potential links to individual descriptive pages
- Agenda
- Our Charter
- The Team
- Contact
- Blog

Required Features:
- Space for photos and videos
- Sections for testimonials and press articles
- Blog/article layout with strong readability
- Easy-to-update backend for future content
- Newsletter sign-up (pop-up and in footer)
- Additional pop-up on/off
- “Request info” buttons
- “Booking request” buttons
- Integration of our 4 pillars - Breathe · Feel · Connect · Experience - in the design (They’re currently in the footer, but we’re open to creative suggestions)

Who we are :
Gather Your Light offers well-being and personal growth stays but with a very different spirit.
We’re not a classic wellness brand. Our approach is professional, joyful, and grounded.
We create spaces where people can take a real break — breathe, slow down, and reconnect with themselves.
During our stays, people are welcomed like friends:
with warmth, respect, and no pressure.
Each program combines practices like breathwork, movement, creativity, coaching, and massages in a relaxed, beautiful setting of the French Alps.
What makes us different:
A friendly and down-to-earth atmosphere
A wide mix of activities.
A mix of inner work and simple pleasures
Private rooms, nourishing food, and shared moments
Time to talk, to laugh, to walk, or just be silent together - and feel free to be yourself
Our guests come to pause.
They leave feeling lighter, aligned, and full of life

```html
<!DOCTYPE html>
<html lang="en">
<head>
<meta charset="utf-8">
<title>Gather Your Light – Well-being Retreats</title>
<link rel="stylesheet" href="https://fonts.googleapis.com/css2?family=Poppins:ital,wght@0,400;0,500;0,600;0,700;0,800;1,400&display=swap">
<style>
:root{
  --navy:#1e3f93;
  --blue:#1f48a3;
  --teal:#5cc4bd;
  --teal-pale:#dff2f0;
  --blue-pale:#e4eaf8;
  --text:#6d7282;
  --white:#ffffff;
  --peach:#f3b27c;
  --pink:#df4f9c;
  --red:#e2545f;
  --gold:#f2a91f;
}
*{box-sizing:border-box;margin:0;padding:0}
html,body{width:1200px;height:5038px;overflow:hidden}
body{position:relative;background:var(--white);font-family:'Poppins',sans-serif;color:var(--text)}
.abs{position:absolute}
.btn{display:inline-flex;align-items:center;justify-content:center;background:var(--teal);color:var(--white);font-weight:600;font-size:11px;letter-spacing:.3px;border-radius:40px;text-transform:uppercase;text-decoration:none}
.photo{display:block}
h2.section-title{font-weight:600;color:var(--navy);font-size:38px;letter-spacing:-.3px}

/* header */
.site-header{top:0;left:0;width:1200px;height:78px;background:var(--white)}
.brand{left:88px;top:24px;font-weight:700;font-size:21px;color:var(--navy);letter-spacing:.2px}
.main-nav{left:318px;top:28px;display:flex;align-items:center;gap:27px;font-size:11px;color:var(--navy);font-weight:500}
.main-nav a{color:inherit;text-decoration:none}
.booking{left:973px;top:18px;width:137px;height:42px;font-size:10px}

/* hero */
.hero{top:78px;left:0;width:1200px;height:622px}
.hero-title{left:86px;top:170px;color:var(--white);font-weight:700;line-height:1}
.hero-title .big{display:block;font-size:112px;letter-spacing:-1px}
.hero-title .sub{display:block;font-size:64px;margin-top:6px;letter-spacing:-.5px}
.hero-text{left:86px;top:369px;width:440px;color:var(--white);font-size:16px;line-height:24px}
.hero .btn{left:86px;top:440px;width:162px;height:39px;font-size:11px}

/* intro */
.intro-mark{left:566px;top:778px;width:68px;height:68px;border-radius:50%;background:radial-gradient(circle,#bfe6e2 0 30%,#e9f6f5 60%,#fff 100%)}
.intro-text{left:210px;top:872px;width:780px;text-align:center;font-size:18.5px;line-height:29px;color:#6e7280}

/* decorations */
.diamond{border-radius:70px;transform:rotate(45deg)}

/* history */
.history-photo{left:143px;top:1081px;width:416px;height:463px;border-radius:42px;border:5px solid #fff;box-shadow:0 12px 30px rgba(30,63,147,.15);background:linear-gradient(160deg,#dfe6d6 0%,#b9c7a8 35%,#7d8c66 70%,#d6d4c8 100%)}
.history{left:618px;top:1128px;width:430px}
.history h2{margin-bottom:20px}
.history p{font-size:12.5px;line-height:21px;margin-bottom:12px}
.history .btn{width:140px;height:39px;margin-top:8px}

/* pillars */
.pillar{top:1644px;width:108px;text-align:center}
.pillar .tile{width:108px;height:107px;border-radius:10px}
.pillar span{display:block;margin-top:22px;font-weight:500;font-size:20px}

/* carousel */
.slide{top:1943px;height:448px;border-radius:20px}
.play{left:555px;top:2121px;width:90px;height:90px;border-radius:50%;background:rgba(255,255,255,.85);display:flex;align-items:center;justify-content:center}

/* charter */
.charter{left:147px;top:2560px;width:410px}
.charter h2{margin-bottom:28px}
.charter h3{font-size:16px;color:var(--navy);font-weight:600;margin-bottom:12px}
.charter p{font-size:12.5px;line-height:21px;margin-bottom:22px}
.charter .btn{width:140px;height:39px}
.charter-photo{left:635px;top:2522px;width:417px;height:438px;border-radius:44px;border:5px solid #fff;box-shadow:0 12px 30px rgba(30,63,147,.15);background:linear-gradient(180deg,#eef1f3 0%,#c9d2da 40%,#8b8a76 70%,#6f6a58 100%)}

/* stays */
.stays{left:61px;top:3057px;width:1079px;height:222px;border:2px solid #c3cdea;border-radius:36px;background:#f3f5fb}
.stay{top:44px;width:135px;height:135px;border-radius:12px;border:2px solid;display:flex;align-items:center;justify-content:center;text-align:center;font-size:14px;line-height:20px;font-weight:500}

/* impact cards */
.card{top:3433px;width:260px;height:359px;background:#fff;box-shadow:0 8px 26px rgba(30,63,147,.12);border-radius:4px;overflow:hidden}
.card .thumb{height:189px}
.card .body{padding:20px 22px 0 22px}
.card h3{font-size:14px;color:var(--navy);font-weight:600;border-left:3px solid var(--navy);padding-left:20px;margin-left:-22px;line-height:18px}
.card p{font-size:12px;line-height:18px;margin-top:12px}
.card a{display:inline-block;margin-top:14px;font-size:11px;font-weight:600;color:var(--teal);text-decoration:underline}

/* testimonial */
.guest-photo{left:156px;top:3888px;width:352px;height:352px;border-radius:50%;background:linear-gradient(150deg,#d7e6c4 0%,#a9c28a 40%,#e8d8c3 70%,#92ad74 100%)}
.guest-accent{left:438px;top:4167px;width:74px;height:37px;border-radius:74px 74px 0 0;background:var(--teal)}
.quote-mark{left:655px;top:3830px;font-size:300px;line-height:1;color:#e3eff6;font-weight:700}
.testimonial{left:569px;top:3960px;width:440px}
.testimonial blockquote{margin-top:28px;font-style:italic;font-size:18.5px;line-height:27px;color:#6e7280}
.testimonial .author{margin-top:26px;font-size:13px;color:var(--navy);display:flex;justify-content:space-between;align-items:center}
.testimonial .author b{font-weight:600}
.dots{margin-top:22px;display:flex;gap:8px}
.dots i{display:block;width:22px;height:3px;background:#c9d4ea;border-radius:2px}
.dots i.on{background:var(--teal)}

/* newsletter & footer */
.newsletter{left:133px;top:4339px;width:934px;height:153px;border-radius:80px;background:var(--teal);box-shadow:0 10px 26px rgba(30,63,147,.18)}
.newsletter h2{position:absolute;left:78px;top:38px;font-size:60px;color:#fff;font-weight:700;letter-spacing:-.5px}
.signup{position:absolute;left:459px;top:53px;width:417px;height:48px;background:#fff;border-radius:30px;display:flex;align-items:center;padding-left:26px;font-size:11px;color:#8b90a0}
.signup svg{margin-right:10px}
.signup .go{position:absolute;right:5px;top:5px;width:128px;height:38px;background:var(--blue);color:#fff;border-radius:24px;font-weight:600;font-size:11px;display:flex;align-items:center;justify-content:center}

.footer-brand{left:131px;top:4740px;font-weight:700;font-size:30px;color:#fff;letter-spacing:.3px;width:300px}
.footer-col{top:4634px;color:#fff}
.footer-col h4{font-size:17px;font-weight:600;margin-bottom:22px}
.footer-col ul{list-style:none}
.footer-col li{font-size:12.5px;line-height:25px}
.footer-col li::before{content:"›";margin-right:7px}
.contact-item{display:flex;gap:12px;font-size:12.5px;line-height:19px;margin-bottom:20px}
.contact-item svg{flex:none;margin-top:3px}
.footer-rule{left:0;top:4955px;width:1200px;height:1px;background:rgba(255,255,255,.18)}
.copyright{left:0;top:4971px;width:1200px;text-align:center;font-size:12.5px;color:#fff}
.to-top{left:1133px;top:4951px;width:40px;height:40px;border-radius:50%;background:var(--teal);display:flex;align-items:center;justify-content:center}
</style>
</head>
<body>

<!-- decorative diamonds -->
<div class="abs diamond" style="left:-160px;top:1080px;width:420px;height:420px;background:var(--teal-pale)"></div>
<div class="abs diamond" style="left:1080px;top:1640px;width:210px;height:210px;background:var(--blue-pale)"></div>
<div class="abs diamond" style="left:-150px;top:3330px;width:310px;height:310px;background:#eef7f6"></div>

<header class="abs site-header">
  <div class="abs brand">Gather Your Light</div>
  <nav class="abs main-nav">
    <svg width="14" height="13" viewBox="0 0 14 13" aria-label="Home"><path d="M7 0 0 6h2v7h4V9h2v4h4V6h2z" fill="var(--teal)"/></svg>
    <a>Our Story</a><a>Our Stays</a><a>Activities</a><a>Agenda</a><a>Our Charter</a><a>The Team</a><a>Blog</a><a>Contact</a>
  </nav>
  <a class="abs btn booking">Booking Request</a>
</header>

<section class="abs hero">
  <svg class="abs" width="1200" height="622" viewBox="0 0 1200 622" style="left:0;top:0">
    <g role="img" aria-label="Photo of a woman with arms open, breathing in the fresh air of an alpine meadow">
      <defs>
        <linearGradient id="heroPhoto" x1="0" y1="0" x2="0" y2="1">
          <stop offset="0" stop-color="#b9c8c2"/>
          <stop offset=".35" stop-color="#8aa07c"/>
          <stop offset=".7" stop-color="#6f8a4e"/>
          <stop offset="1" stop-color="#5a7440"/>
        </linearGradient>
      </defs>
      <path d="M540 0H1200V622H760L500 60Q490 0 540 0Z" fill="url(#heroPhoto)"/>
    </g>
    <path d="M0 0H455Q478 0 488 22L718 560Q740 622 680 622H0Z" fill="var(--blue)"/>
  </svg>
  <h1 class="abs hero-title"><span class="big">Gather</span><span class="sub">Your Light</span></h1>
  <p class="abs hero-text">Well-being retreats in the heart of the French Alps – where rest meets reconnection.</p>
  <a class="abs btn">Get an Estimate</a>
</section>

<div class="abs intro-mark" role="img" aria-label="Small teal mandala emblem"></div>
<p class="abs intro-text">Imagine a space designed to allow for a true break, where every breath counts. Through its retreats, Gather Your Light invites you on an inner and outer journey, a unique experience where each step reconnects you with your vitality and well-being.</p>

<div class="abs photo history-photo" role="img" aria-label="Portrait of a smiling older woman sitting cross-legged among white flowers"></div>
<section class="abs history">
  <h2 class="section-title">Our History</h2>
  <p>Gather Your Light, is above all, a story of men and women, a story of encounters and desire, a desire to share, a desire to refocus and a desire to breathe.</p>
  <p>Absorbed in a world that is running out of time, it has become essential to find a little personal space to take precisely the time we are so desperately running after.</p>
  <p>Through our fiduciary activities at GATHER The Future and GATHER The Solution, we have been able to observe the growing imbalance in most of our lives and the desire was born to create this bubble of respite in a world that is constantly agitated.</p>
  <a class="btn">Read More</a>
</section>

<div class="abs pillar" style="left:285px"><div class="tile" style="background:#fdf0e3" role="img" aria-label="Breathe pillar icon"></div><span style="color:var(--peach)">Breathe</span></div>
<div class="abs pillar" style="left:468px"><div class="tile" style="background:#dfe6f8" role="img" aria-label="Feel pillar icon"></div><span style="color:#4d6ec4">Feel</span></div>
<div class="abs pillar" style="left:650px"><div class="tile" style="background:var(--pink)" role="img" aria-label="Connect pillar icon"></div><span style="color:var(--pink)">Connect</span></div>
<div class="abs pillar" style="left:833px"><div class="tile" style="background:#e1f3f2" role="img" aria-label="Experience pillar icon"></div><span style="color:var(--teal)">Experience</span></div>

<h2 class="abs section-title" style="left:0;width:1200px;text-align:center;top:1862px">Our Impact</h2>
<div class="abs slide" style="left:-20px;width:229px;background:linear-gradient(160deg,#d7dde4,#9aa6b2 50%,#6a6a62)" role="img" aria-label="Photo of a woman resting on a rock above a valley"></div>
<div class="abs slide" style="left:229px;width:742px;background:linear-gradient(180deg,#7f9b6a 0%,#9fb3b0 35%,#6c8a6a 65%,#3e5a38 100%)" role="img" aria-label="Video still of a man with arms spread wide facing a lake"></div>
<div class="abs slide" style="left:991px;width:229px;background:linear-gradient(160deg,#9cb07a,#5f7a44 60%,#d8d6c8)" role="img" aria-label="Photo of an older man pointing toward the sky"></div>
<div class="abs play"><svg width="22" height="24" viewBox="0 0 22 24"><path d="M2 1 21 12 2 23Z" fill="var(--navy)"/></svg></div>

<section class="abs charter">
  <h2 class="section-title">Our Charter</h2>
  <h3>1. Respect and Diversity</h3>
  <p>I commit to treating myself and all other participants, speakers, and interlocutors with respect, inclusivity, listening, and kindness, without judgment or projection.</p>
  <h3>2. Sharing and Confidentiality</h3>
  <p>I promise to let everyone express themselves freely and share their opinions and experiences with respect for others and themselves.</p>
  <a class="btn">Read More</a>
</section>
<div class="abs photo charter-photo" role="img" aria-label="Photo of a person meditating with raised hands on a mountain rock"></div>

<section class="abs stays">
  <div class="abs stay" style="left:81px;background:#fdeedd;border-color:#f5d3ae;color:var(--peach)">Instant<br>Workshops</div>
  <div class="abs stay" style="left:276px;background:#d6dff9;border-color:#8fa7e4;color:var(--navy)">6-night<br>flight</div>
  <div class="abs stay" style="left:470px;background:#f7d4ea;border-color:#e7a2cd;color:var(--pink)">4-night<br>getaway</div>
  <div class="abs stay" style="left:665px;background:#daf0ee;border-color:#98d5cf;color:var(--teal)">2-night<br>break</div>
  <div class="abs stay" style="left:859px;background:#fbdadd;border-color:#ef9aa2;color:var(--red)">1 day<br>break</div>
</section>

<h2 class="abs section-title" style="left:0;width:1200px;text-align:center;top:3356px">Our Impact</h2>
<article class="abs card" style="left:193px"><div class="thumb" style="background:linear-gradient(180deg,#dfe6ea,#a6b3b6 50%,#5f6a5e)" role="img" aria-label="Photo of a woman in pink meditating by a waterfall"></div><div class="body"><h3>Some Heading Goes Here</h3><p>commit to treating myself &amp; all other participants, speakers, &amp; interlocutors with.</p><a>READ MORE</a></div></article>
<article class="abs card" style="left:469px"><div class="thumb" style="background:linear-gradient(180deg,#dfe8d6,#9fb585 50%,#6f8a4f)" role="img" aria-label="Photo of an older woman meditating in a garden"></div><div class="body"><h3>Some Heading Goes Here</h3><p>commit to treating myself &amp; all other participants, speakers, &amp; interlocutors with.</p><a>READ MORE</a></div></article>
<article class="abs card" style="left:745px"><div class="thumb" style="background:linear-gradient(180deg,#c9cfcf,#7d8478 50%,#3f4540)" role="img" aria-label="Photo of a smiling older man outdoors"></div><div class="body"><h3>Some Heading Goes Here</h3><p>commit to treating myself &amp; all other participants, speakers, &amp; interlocutors with.</p><a>READ MORE</a></div></article>

<div class="abs guest-photo" role="img" aria-label="Photo of a joyful woman in a hat with arms raised under trees"></div>
<div class="abs guest-accent"></div>
<div class="abs quote-mark" aria-hidden="true">“</div>
<section class="abs testimonial">
  <h2 class="section-title">What Our Guests Say</h2>
  <blockquote>"This retreat was exactly what I needed - space to breathe, move, and just be. I felt seen &amp; supported every step of the way."</blockquote>
  <div class="author"><span><b>ELENA V.,</b> SCHOOL TEACHER</span>
    <svg width="80" height="14" viewBox="0 0 80 14" aria-label="Five stars"><g fill="var(--gold)"><path id="st" d="M7 0l2 4.5 5 .5-3.7 3.3 1 5L7 10.8 2.7 13.3l1-5L0 5l5-.5z"/><use href="#st" x="16.5"/><use href="#st" x="33"/><use href="#st" x="49.5"/><use href="#st" x="66"/></g></svg>
  </div>
  <div class="dots"><i></i><i class="on"></i><i></i></div>
</section>

<svg class="abs" style="left:0;top:4330px" width="1200" height="708" viewBox="0 0 1200 708">
  <path d="M0 340C320 250 640 190 930 90C1040 40 1090 0 1150 0Q1200 0 1200 20V708H0Z" fill="var(--blue)"/>
</svg>

<section class="abs newsletter">
  <h2>Newsletter</h2>
  <div class="signup">
    <svg width="13" height="10" viewBox="0 0 13 10"><rect width="13" height="10" rx="1.5" fill="var(--teal)"/><path d="M1 1.5 6.5 5.5 12 1.5" stroke="#fff" stroke-width="1.2" fill="none"/></svg>
    Enter your email address..
    <span class="go">READ MORE</span>
  </div>
</section>

<div class="abs footer-brand">Gather Your Light</div>
<div class="abs footer-col" style="left:438px">
  <h4>Quick Links</h4>
  <ul><li>Home</li><li>Our Story</li><li>Our Stays</li><li>Activities</li><li>Agenda</li><li>Our Charter</li><li>The Team</li><li>Blog</li><li>Contact</li></ul>
</div>
<div class="abs footer-col" style="left:633px">
  <h4>Services</h4>
  <ul style="margin-top:8px"><li>Instant Workshops</li><li>6-night flight</li><li>4-night getaway</li><li>2-night break</li><li>1 day break</li></ul>
</div>
<div class="abs footer-col" style="left:854px;width:250px">
  <h4>Contact info</h4>
  <div class="contact-item" style="margin-top:8px"><svg width="13" height="10" viewBox="0 0 13 10"><rect width="13" height="10" rx="1.5" fill="#fff"/><path d="M1 1.5 6.5 5.5 12 1.5" stroke="var(--blue)" stroke-width="1.2" fill="none"/></svg><span>Email:<br>info@gatheryourlight.ch</span></div>
  <div class="contact-item"><svg width="13" height="13" viewBox="0 0 24 24"><path d="M6.6 10.8a15 15 0 0 0 6.6 6.6l2.2-2.2c.3-.3.7-.4 1-.2 1.1.4 2.3.6 3.6.6.6 0 1 .4 1 1V20c0 .6-.4 1-1 1A17 17 0 0 1 3 4c0-.6.4-1 1-1h3.5c.6 0 1 .4 1 1 0 1.3.2 2.5.6 3.6.1.3 0 .7-.2 1z" fill="#fff"/></svg><span>Phone:<br>+41 58 200 41 70</span></div>
  <div class="contact-item"><svg width="12" height="15" viewBox="0 0 12 15"><path d="M6 0a6 6 0 0 0-6 6c0 4.5 6 9 6 9s6-4.5 6-9a6 6 0 0 0-6-6zm0 8.2A2.2 2.2 0 1 1 6 3.8a2.2 2.2 0 0 1 0 4.4z" fill="#fff"/></svg><span>Location:<br>Gather Your Light Sàrl Chemin des Prés 8, Building B2<br>CH - 1260 Nyon</span></div>
</div>
<div class="abs footer-rule"></div>
<p class="abs copyright">© Copyright 2025 Gather Your Light All Right Reserved</p>
<div class="abs to-top"><svg width="14" height="9" viewBox="0 0 14 9"><path d="M1 8 7 2l6 6" stroke="#fff" stroke-width="2" fill="none"/></svg></div>

</body>
</html>
```